Estate Planner needs an Ad for a local newsletter

I need an ad designed for my practice as an estate planning attorney. The ad will be in a newsletter that targets individuals over the age of 55. My ad is 7.5"W x 4.6"H (a half page ad) .
The wording should include:
Varnholt, Danielle

Danielle Varnholt

Wisdom Meets Planning
Your Estate, Your Legacy

After 23 years as a military spouse, moving our family of six across the country,
I learned the true value of careful planning. Today I help Palomar County's seniors protect what matters most – their family’s future and their life’s work.

I understand that your estate is more than just assets – it's a lifetime of wise
decisions, cherished memories, and dreams for your family's future.

Professional Estate Planning:
• Wills & Living Trusts • Healthcare Directives
• Power of Attorney • Asset Protection
• Probate Avoidance • Peace of Mind

Plus also needs to have my contact information:
RPV Law
Danielle Varnholt
Attorney/Of Counsel
4712 Cedarbrook Lane
Ashford Vale, Oregon 97412
(555) 684-1093
dvarnholt@rpvlegalteam.example
Logo is attached.

```html
<!DOCTYPE html>
<html lang="en">
<head>
<meta charset="utf-8">
<title>RPV Law – Estate Planning Advert</title>
<link rel="stylesheet" href="https://fonts.googleapis.com/css2?family=Poppins:wght@400;500;600;700&display=swap">
<style>
  :root {
    --navy: #0b3f78;
    --ink: #16202e;
    --band: #235b91;
    --tab: #11325a;
    --cyan: #35aeea;
    --sky-deep: #b6def6;
    --sky-pale: #eef8fd;
    --quote: #cfe9fb;
    --white: #ffffff;
    --rule: #2a4f7e;
  }
  * { margin: 0; padding: 0; box-sizing: border-box; }
  html, body {
    width: 1200px; height: 793px; overflow: hidden;
    background: var(--white);
    font-family: "Poppins", sans-serif;
    color: var(--ink);
  }
  .advert { position: relative; width: 1200px; height: 793px; overflow: hidden; }

  /* hero */
  .hero {
    position: absolute; left: 0; top: 0; width: 1200px; height: 519px;
    background: linear-gradient(100deg, var(--sky-deep) 0%, #cbe9f9 40%, var(--sky-pale) 62%, #f7fbfd 75%);
  }
  .hero-photo {
    position: absolute; left: 591px; top: 0; width: 609px; height: 519px;
    background: linear-gradient(90deg, rgba(240,248,252,0) 0%, #c9d9e2 18%, #6f86a6 45%, #a9a08e 70%, #b99567 100%);
  }
  .brand {
    position: absolute; left: 57px; top: 44px;
    display: flex; align-items: center; gap: 14px;
    font-weight: 600; font-size: 48px; color: var(--navy); letter-spacing: -0.5px;
  }
  .brand-mark { width: 30px; height: 30px; background: var(--navy); }
  .headline {
    position: absolute; left: 55px; top: 178px;
    font-weight: 700; font-size: 54px; line-height: 56px;
    color: var(--navy); letter-spacing: -0.5px; text-transform: uppercase;
  }
  .tagline {
    position: absolute; left: 57px; top: 302px; width: 424px;
    border-top: 2px solid var(--rule); border-bottom: 2px solid var(--rule);
    padding: 6px 0 4px;
    font-weight: 500; font-size: 28.5px; line-height: 36px;
    color: var(--ink); text-transform: uppercase; letter-spacing: -0.3px;
  }
  .story {
    position: absolute; left: 59px; top: 374px; width: 462px;
    font-size: 17.4px; line-height: 23px; color: var(--ink);
  }

  /* service band */
  .band {
    position: absolute; left: 0; top: 519px; width: 1200px; height: 148px;
    background: var(--band);
  }
  .band-tab { position: absolute; left: 700px; top: 506px; width: 418px; height: 40px; }
  .band-tab-label {
    position: absolute; left: 715px; top: 506px; width: 387px; height: 39px;
    display: flex; align-items: center; justify-content: center;
    font-weight: 700; font-size: 19px; color: var(--cyan); letter-spacing: -0.2px;
  }
  .quote {
    position: absolute; left: 266px; top: 556px; width: 330px;
    font-size: 16px; line-height: 21px; color: var(--quote);
  }
  .band-divider {
    position: absolute; left: 622px; top: 565px; width: 1px; height: 82px;
    background: rgba(255,255,255,0.25);
  }
  .services { position: absolute; top: 564px; list-style: none; }
  .services li {
    position: relative; padding-left: 15px;
    font-size: 20px; line-height: 25.5px; color: var(--white);
  }
  .services li::before {
    content: ""; position: absolute; left: 0; top: 9px;
    width: 7px; height: 7px; border: 2px solid var(--cyan); border-radius: 50%;
  }
  .services-left { left: 670px; }
  .services-right { left: 911px; }

  /* attorney portrait */
  .portrait-ring {
    position: absolute; left: 36px; top: 538px; width: 196px; height: 196px;
    border-radius: 50%; background: var(--white);
    box-shadow: 0 -4px 0 0 #bfe4f8;
  }
  .portrait {
    position: absolute; left: 48px; top: 546px; width: 172px; height: 186px;
    border-radius: 50% 50% 48% 48%;
    background: radial-gradient(circle at 50% 40%, #e8c3ad 0%, #b98566 40%, #6b4630 70%, #2f3650 100%);
  }

  /* contact strip */
  .contact-name { position: absolute; left: 266px; top: 683px; }
  .contact-name .firm { font-size: 17px; line-height: 22px; }
  .contact-name .attorney { font-weight: 700; font-size: 21px; line-height: 26px; color: var(--navy); }
  .contact-name .role { font-size: 17px; line-height: 22px; }
  .contact-divider { position: absolute; top: 690px; width: 1px; height: 66px; background: #d3d9e0; }
  .contact-divider.first { left: 504px; }
  .contact-divider.second { left: 875px; }
  .contact-lines { position: absolute; list-style: none; }
  .contact-lines li {
    display: flex; align-items: center; gap: 8px;
    font-size: 17px; line-height: 25px; color: var(--ink);
  }
  .contact-lines svg { flex: none; }
  .contact-lines strong { font-weight: 600; }
  .contact-reach { left: 537px; top: 700px; }
  .contact-address { left: 906px; top: 700px; }
  .contact-address .city { padding-left: 23px; line-height: 21px; }
</style>
</head>
<body>
<main class="advert">

  <section class="hero">
    <div class="hero-photo" role="img" aria-label="Photo of a smiling senior couple taking a selfie outdoors by the water"></div>
    <div class="brand"><span class="brand-mark"></span>RPV Law</div>
    <h1 class="headline">Wisdom Meets<br>Planning</h1>
    <h2 class="tagline">Your Estate, Your Legacy</h2>
    <p class="story">After 23 years as a military spouse, moving our family of six across the country, I learned the true value of careful planning. Today I help Palomar County’s seniors protect what matters most – their family’s future and their life’s work.</p>
  </section>

  <section class="band"></section>
  <svg class="band-tab" viewBox="0 0 418 40" aria-hidden="true">
    <polygon points="0,13 15,0 15,13" fill="var(--cyan)"/>
    <polygon points="403,0 418,13 403,13" fill="var(--cyan)"/>
    <path d="M15,0 H403 L399,30 Q397,39 388,39 H30 Q21,39 19,30 Z" fill="var(--tab)"/>
  </svg>
  <div class="band-tab-label">PROFESSIONAL ESTATE PLANNING</div>

  <p class="quote">I understand that your estate is more than just assets – it’s a lifetime of wise decisions, cherished memories, and dreams for your family’s future.</p>
  <div class="band-divider"></div>
  <ul class="services services-left">
    <li>Wills &amp; Living Trusts</li>
    <li>Power of Attorney</li>
    <li>Probate Avoidance</li>
  </ul>
  <ul class="services services-right">
    <li>Healthcare Directives</li>
    <li>Asset Protection</li>
    <li>Peace of Mind</li>
  </ul>

  <div class="portrait-ring"></div>
  <div class="portrait" role="img" aria-label="Portrait photo of attorney Danielle Varnholt"></div>

  <div class="contact-name">
    <p class="firm">RPV Law</p>
    <p class="attorney">Danielle Varnholt</p>
    <p class="role">Attorney/Of Counsel</p>
  </div>
  <div class="contact-divider first"></div>
  <ul class="contact-lines contact-reach">
    <li>
      <svg width="17" height="17" viewBox="0 0 20 20" aria-hidden="true"><circle cx="10" cy="10" r="9" fill="none" stroke="var(--navy)" stroke-width="2"/><path d="M7 5.5l1.6 2.4-1 1.2a6 6 0 0 0 3.3 3.3l1.2-1 2.4 1.6-.8 1.7c-3.9-.3-7.5-3.9-7.800-7.8z" fill="var(--navy)"/></svg>
      <span>Call us <strong>(555) 684-1093</strong></span>
    </li>
    <li>
      <svg width="17" height="17" viewBox="0 0 20 20" aria-hidden="true"><circle cx="10" cy="10" r="10" fill="var(--navy)"/><rect x="5" y="6.5" width="10" height="7" rx="1" fill="none" stroke="#fff" stroke-width="1.3"/><path d="M5.3 7l4.7 3.6L14.7 7" fill="none" stroke="#fff" stroke-width="1.3"/></svg>
      <span>dvarnholt@rpvlegalteam.example</span>
    </li>
  </ul>
  <div class="contact-divider second"></div>
  <ul class="contact-lines contact-address">
    <li class="street">
      <svg width="15" height="18" viewBox="0 0 16 20" aria-hidden="true"><path d="M8 0a7 7 0 0 0-7 7c0 5 7 13 7 13s7-8 7-13a7 7 0 0 0-7-7z" fill="var(--navy)"/><circle cx="8" cy="7" r="2.6" fill="#fff"/></svg>
      <span>4712 Cedarbrook Lane</span>
    </li>
    <li class="city">Ashford Vale, Oregon 97412</li>
  </ul>

</main>
</body>
</html>
```